Up to the Challenge? Canadian based consulting company needs a two sided business card design

A Canadian based security risk management consulting company needs a two-sided business card design. What we do is provide advice and guidance related to emergency, security and business continuity management for small, medium and large companies to help ensure the protection of their people, assets, information, services, operations and reputation.

The final design should be simple, only one or two colours, eye catching, professional and one that makes people look at three or more times just because it looks so darn good.

I have include examples of business cards I like.

Target Market(s)

Small, medium and large companies.

Industry/Entity Type

Security

Contact Information for Business Card

Business Card Size: Standard size of 3.5" (89mm) x 2.0" (51mm) - (see full specifications and guides on PRINTA's website if required)
Card Stock: Looking to use PRINTA's Velda 32pt stock textured paper - seam colour either chili red or black
Business Name: The Harrowfield Group
Website: www.theharrowfieldgroup.example
Telephone: (555)214-0397
Name: Dana Forsythe
Position: Principle
e-mail: Dana.Forsythe@theharrowfieldgroup.example

Font styles to use
Serif

Colors
ec1f27
000000
9d9d9d
aaaaaa
606060

Requirements
Must have
• - "The Harrowfield Group" logo (see uploaded files). I have included grey scale and colour versions.
• - Business card details (as above)
Nice to have
• - One side black or grey scale.
• - Other side would likely be white.
• - Everyone likes the silver logo on the black background.
• - Small element of colour i.e. red but I'm leaning more to greyscale.
Should not have
• - A lot of colour. Keep it simple.

```html
<!DOCTYPE html>
<html lang="en">
<head>
<meta charset="utf-8">
<title>The Harrowfield Group – Business Card</title>
<link rel="stylesheet" href="https://fonts.googleapis.com/css2?family=Cinzel:wght@400;500&family=Open+Sans:wght@400;600&display=swap">
<style>
  :root {
    --page: #e7e5e2;
    --card-black: #111111;
    --card-black-edge: #1d1d1d;
    --silver: #aaaaaa;
    --silver-light: #c9c9c9;
    --card-white: #f4f4f4;
    --tab: #1a1a1a;
    --ink: #606060;
    --ink-dark: #4a4a4a;
    --accent: #9d9d9d;
    --watermark: #e2e2e2;
  }
  * { margin: 0; padding: 0; box-sizing: border-box; }
  html, body { width: 1200px; height: 1023px; overflow: hidden; }
  body {
    background: var(--page);
    position: relative;
    font-family: "Open Sans", Arial, sans-serif;
  }
  .card {
    position: absolute;
    left: 320px;
    width: 560px;
    height: 320px;
    border-radius: 18px;
    overflow: hidden;
    box-shadow: 0 6px 18px rgba(0,0,0,0.18);
  }

  /* Front */
  .card-front {
    top: 130px;
    background: linear-gradient(135deg, var(--card-black-edge), var(--card-black));
    display: flex;
    align-items: center;
    justify-content: center;
    gap: 26px;
  }
  .brand-square {
    width: 74px;
    height: 74px;
    background: var(--silver);
    border-radius: 4px;
    flex: none;
  }
  .brand-name {
    font-family: "Cinzel", "Times New Roman", serif;
    font-weight: 400;
    color: var(--silver);
    font-size: 34px;
    line-height: 1.15;
    letter-spacing: 2px;
    text-transform: uppercase;
  }

  /* Back */
  .card-back {
    top: 560px;
    background: var(--card-white);
  }
  .name-tab {
    position: absolute;
    top: 0;
    left: 40px;
    width: 300px;
    height: 88px;
    background: var(--tab);
    border-radius: 0 0 30px 30px;
    padding: 16px 0 0 34px;
    color: #ffffff;
  }
  .person-name {
    font-weight: 600;
    font-size: 26px;
    line-height: 1.1;
  }
  .person-role {
    font-size: 15px;
    color: var(--silver-light);
    margin-top: 2px;
  }
  .contact-list {
    position: absolute;
    top: 106px;
    left: 52px;
    list-style: none;
  }
  .contact-item {
    display: flex;
    align-items: center;
    gap: 12px;
    font-size: 15px;
    color: var(--ink);
    height: 25px;
  }
  .contact-icon {
    width: 14px;
    height: 14px;
    flex: none;
  }
  .contact-icon path, .contact-icon circle, .contact-icon rect { fill: none; stroke: var(--ink-dark); stroke-width: 1.4; }
  .contact-icon .solid { fill: var(--ink-dark); stroke: none; }
  .watermark {
    position: absolute;
    right: 28px;
    bottom: 14px;
    font-family: "Cinzel", "Times New Roman", serif;
    font-weight: 400;
    font-size: 24px;
    letter-spacing: 2px;
    color: var(--watermark);
    text-transform: uppercase;
    text-align: right;
    line-height: 1.1;
  }
</style>
</head>
<body>

<section class="card card-front" aria-label="Card front">
  <div class="brand-square"></div>
  <div class="brand-name">The Harrowfield<br>Group</div>
</section>

<section class="card card-back" aria-label="Card back">
  <div class="watermark">The Harrowfield<br>Group</div>

  <div class="name-tab">
    <div class="person-name">Dana Forsythe</div>
    <div class="person-role">Principle</div>
  </div>

  <ul class="contact-list">
    <li class="contact-item">
      <svg class="contact-icon" viewBox="0 0 14 14"><path class="solid" d="M7 0.5a4.5 4.5 0 0 0-4.5 4.5c0 3.4 4.5 8.5 4.5 8.5s4.5-5.1 4.5-8.5A4.5 4.5 0 0 0 7 0.5z"/><circle cx="7" cy="5" r="1.5" style="fill:#fff;stroke:none"/></svg>
      <span>Your address</span>
    </li>
    <li class="contact-item">
      <svg class="contact-icon" viewBox="0 0 14 14"><circle cx="7" cy="7" r="6"/><path d="M5 4.2l1.2 1.6-0.8 0.9c0.5 1 1.1 1.6 2 2l0.9-0.8 1.6 1.2-0.8 1.1c-2.4-0.3-4.6-2.5-4.9-4.9z"/></svg>
      <span>(555)214-0397</span>
    </li>
    <li class="contact-item">
      <svg class="contact-icon" viewBox="0 0 14 14"><rect x="1" y="3" width="12" height="8"/><path d="M1 3l6 5 6-5"/></svg>
      <span>Dana.Forsythe@theharrowfieldgroup.example</span>
    </li>
    <li class="contact-item">
      <svg class="contact-icon" viewBox="0 0 14 14"><circle cx="7" cy="7" r="6"/><path d="M1 7h12M7 1c-2.4 3-2.4 9 0 12M7 1c2.4 3 2.4 9 0 12"/></svg>
      <span>www.theharrowfieldgroup.example</span>
    </li>
    <li class="contact-item">
      <svg class="contact-icon" viewBox="0 0 14 14"><rect class="solid" x="1" y="1" width="12" height="12" rx="2"/></svg>
      <span>https://ca.profilenet.example/in/danaforsythe</span>
    </li>
  </ul>
</section>

</body>
</html>
```